Newspaper ad for web design services

I have a paid space in a local newspaper size: 4.5085" W x 2.6875" H.
I want to use it for promoting my web design services.
Designers have the freedom to design the ad and the offer.
The goal is to have people contact me for business web design.
I published one ad last month and it totally failed to bring any attention.
Feel free to change or add anything you think can be more effective to attract potential customers (I can create any tripwire you consider will work)
Target: Houston-based business owners looking to get a new website or to update their existing one.

```html
<!DOCTYPE html>
<html lang="en">
<head>
<meta charset="utf-8">
<title>Nolan Web Studio – Newspaper Ad</title>
<link href="https://fonts.googleapis.com/css2?family=Nunito+Sans:wght@400;600;800;900&display=swap" rel="stylesheet">
<style>
  :root{
    --navy:#1e2a55;
    --accent:#4a5fb5;
    --accent-text:#3d52b3;
    --white:#ffffff;
    --ink:#1c2233;
    --lavender:#dfe4f7;
    --periwinkle:#9fb0e6;
    --salmon:#f08a7c;
    --photo-light:#9a9186;
    --photo-dark:#2e2b28;
  }
  *{margin:0;padding:0;box-sizing:border-box}
  html,body{width:1200px;height:804px;overflow:hidden;background:var(--navy)}
  .ad{position:relative;width:1200px;height:804px;background:var(--navy);font-family:"Nunito Sans",sans-serif;color:var(--white);overflow:hidden}
  .layer{position:absolute;left:0;top:0}
  .brand{position:absolute;left:59px;top:49px;display:flex;align-items:center;gap:14px}
  .brand-mark{width:52px;height:59px;background:var(--accent);border-radius:8px}
  .brand-name{font-size:50px;font-weight:600;letter-spacing:-0.5px;line-height:1}
  .headline{position:absolute;left:61px;top:150px;font-size:43px;font-weight:900;line-height:57px;letter-spacing:0.4px}
  .benefits{position:absolute;left:61px;top:318px;list-style:none}
  .benefits li{display:flex;align-items:center;height:44.5px;font-size:30px;font-weight:400;letter-spacing:1.3px}
  .benefits svg{width:26px;height:26px;margin-right:23px;flex:none}
  .illustration{position:absolute;left:652px;top:106px}
  .contact{position:absolute;top:588px;height:34px;border-radius:17px;background:var(--accent);display:flex;align-items:center;font-size:21px;font-weight:600;white-space:nowrap}
  .contact .icon{width:34px;height:34px;border-radius:50%;background:var(--white);display:flex;align-items:center;justify-content:center;margin-right:12px;flex:none}
  .contact-web{left:586px;width:326px}
  .contact-phone{left:925px;width:220px;font-size:23px}
  .photo{position:absolute;left:62px;top:588px;width:292px;height:292px;border-radius:50%;background:radial-gradient(circle at 50% 35%,var(--photo-light) 0,#6f675f 45%,var(--photo-dark) 100%)}
  .play{position:absolute;left:181px;top:682px;width:52px;height:52px;border-radius:50%;border:3px solid rgba(255,255,255,.85);background:rgba(255,255,255,.15)}
  .offer{position:absolute;left:517px;top:678px;font-size:27px;line-height:36px;color:var(--ink);font-weight:400;letter-spacing:0.3px}
  .offer strong{color:var(--accent-text);font-weight:800}
</style>
</head>
<body>
<div class="ad">
  <svg class="layer" width="1200" height="804" viewBox="0 0 1200 804">
    <path d="M0 654 H470 C500 654 510 606 540 606 H1200 V804 H0 Z" fill="var(--white)"/>
    <rect x="61" y="283" width="519" height="2" fill="var(--white)"/>
    <rect x="61" y="281" width="138" height="7" fill="var(--accent)"/>
    <circle cx="208" cy="735" r="168" fill="none" stroke="var(--accent)" stroke-width="2.5"/>
  </svg>

  <div class="brand">
    <div class="brand-mark"></div>
    <div class="brand-name">Nolan Web Studio</div>
  </div>

  <h1 class="headline">Time-saving solutions to<br>help your business scale</h1>

  <ul class="benefits">
    <li><svg viewBox="0 0 26 26"><circle cx="12" cy="13" r="10.5" fill="none" stroke="#fff" stroke-width="2"/><path d="M7 13l5 5L24 4" fill="none" stroke="var(--accent)" stroke-width="3" stroke-linecap="round"/></svg>Get more New customers</li>
    <li><svg viewBox="0 0 26 26"><circle cx="12" cy="13" r="10.5" fill="none" stroke="#fff" stroke-width="2"/><path d="M7 13l5 5L24 4" fill="none" stroke="var(--accent)" stroke-width="3" stroke-linecap="round"/></svg>Buy more</li>
    <li><svg viewBox="0 0 26 26"><circle cx="12" cy="13" r="10.5" fill="none" stroke="#fff" stroke-width="2"/><path d="M7 13l5 5L24 4" fill="none" stroke="var(--accent)" stroke-width="3" stroke-linecap="round"/></svg>Get more reviews</li>
    <li><svg viewBox="0 0 26 26"><circle cx="12" cy="13" r="10.5" fill="none" stroke="#fff" stroke-width="2"/><path d="M7 13l5 5L24 4" fill="none" stroke="var(--accent)" stroke-width="3" stroke-linecap="round"/></svg>Refer more customers</li>
  </ul>

  <svg class="illustration" width="504" height="390" viewBox="0 0 504 390" role="img" aria-label="Illustration of designers building a website on a large monitor with colour swatches, a tablet and a keyboard">
    <defs>
      <linearGradient id="sceneTone" x1="0" y1="0" x2="1" y2="1">
        <stop offset="0" stop-color="var(--lavender)"/>
        <stop offset="0.35" stop-color="var(--salmon)"/>
        <stop offset="0.7" stop-color="var(--periwinkle)"/>
        <stop offset="1" stop-color="var(--lavender)"/>
      </linearGradient>
    </defs>
    <path d="M40 40 C80 0 150 20 180 40 C210 60 240 20 280 12 C320 4 340 40 380 30 C430 20 470 40 480 90 C500 150 504 250 490 300 C470 350 430 360 380 370 C320 385 250 390 160 380 C90 372 30 350 12 300 C-4 250 10 200 6 150 C2 100 10 70 40 40 Z" fill="url(#sceneTone)"/>
  </svg>

  <div class="contact contact-web">
    <span class="icon"><svg width="24" height="24" viewBox="0 0 24 24" fill="none" stroke="var(--accent)" stroke-width="1.6"><circle cx="12" cy="12" r="10"/><ellipse cx="12" cy="12" rx="4.5" ry="10"/><path d="M2 12h20M4 6.5h16M4 17.5h16"/></svg></span>
    www.nolanwebstudio.com
  </div>
  <div class="contact contact-phone">
    <span class="icon"><svg width="22" height="22" viewBox="0 0 24 24"><path d="M6.6 10.8a15.1 15.1 0 0 0 6.6 6.6l2.2-2.2a1 1 0 0 1 1-.25 11.4 11.4 0 0 0 3.6.57 1 1 0 0 1 1 1V20a1 1 0 0 1-1 1A17 17 0 0 1 3 4a1 1 0 0 1 1-1h3.5a1 1 0 0 1 1 1c0 1.25.2 2.45.57 3.57a1 1 0 0 1-.25 1z" fill="var(--accent)"/></svg></span>
    281-555-0147
  </div>

  <div class="photo" role="img" aria-label="Video thumbnail of the studio owner in a home studio holding a mug"></div>
  <div class="play"></div>
  <svg class="layer" width="1200" height="804" viewBox="0 0 1200 804">
    <path d="M202 697 L202 721 L221 709 Z" fill="rgba(255,255,255,.85)"/>
    <circle cx="366" cy="724" r="28" fill="var(--accent)"/>
  </svg>

  <p class="offer">Download this <strong>FREE E-Book</strong><br>The <strong>ONE</strong> easy change will make <strong>YOUR BUSINESS</strong><br><strong>WEBSITE</strong> Double Your Sale</p>
</div>
</body>
</html>
```